Business Cards for a law firm

Business cards for our law firm. Use our silhoette logo and OAK HARBOR - check our website (www.oakharbor-legal.com)

Contact Information for Business Card

our silhouette logo, OAK HARBOR, 800-555-0147, Dorian Kestrup, dorian@oakharbor-legal.com

Requirements
Must have
• our silhouette logo, OAK HARBOR, 800-555-0147, Dorian Kestrup, dorian@oakharbor-legal.com

```html
<!DOCTYPE html>
<html lang="en">
<head>
<meta charset="utf-8">
<title>Oak Harbor – Business Cards</title>
<link rel="stylesheet" href="https://fonts.googleapis.com/css2?family=Marcellus&family=Cinzel:wght@700&family=Barlow:wght@500&display=swap">
<style>
  :root {
    --navy: #1b2f6b;
    --orange: #f5a623;
    --ink-grey: #56595e;
    --paper: #ffffff;
    --ghost: #f4f5f7;
    --backdrop: #e4e5e7;
  }
  * { margin: 0; padding: 0; box-sizing: border-box; }
  html, body { width: 807px; height: 1200px; overflow: hidden; background: var(--backdrop); }
  .canvas { position: relative; width: 807px; height: 1200px; }

  .card {
    position: absolute; left: 53px; width: 702px; height: 422px;
    background: var(--paper); border: 23px solid var(--navy);
  }
  .card--front { top: 167px; }
  .card--back { top: 635px; }

  .brand { position: absolute; display: flex; align-items: center; gap: 12px; }
  .brand__square { width: 30px; height: 30px; background: var(--navy); }
  .brand__name {
    font-family: "Marcellus", serif; font-size: 31px; letter-spacing: 1px;
    color: var(--navy); line-height: 1; white-space: nowrap;
  }
  .card--front .brand { left: 48px; top: 271px; }
  .card--back .brand { left: 176px; top: 70px; }

  .figures-backdrop {
    position: absolute; left: 355px; top: 10px; width: 262px; height: 366px;
    background: var(--ghost);
  }

  .holder-name {
    position: absolute; left: 0; right: 0; top: 178px; text-align: center;
    font-family: "Cinzel", serif; font-weight: 700; font-size: 24px;
    color: var(--navy); letter-spacing: 0.5px;
  }
  .divider { position: absolute; left: 141px; top: 234px; }

  .address {
    position: absolute; right: 414px; top: 269px; text-align: right;
    font-family: "Barlow", sans-serif; font-weight: 500; font-size: 13px;
    line-height: 17px; color: var(--navy); white-space: nowrap;
  }
  .contacts { position: absolute; left: 380px; top: 268px; list-style: none; }
  .contacts li {
    display: flex; align-items: center; gap: 10px; height: 19.5px;
    font-family: "Barlow", sans-serif; font-weight: 500; font-size: 13px;
    color: var(--ink-grey); letter-spacing: 0.4px;
  }
  .contacts svg { width: 12px; height: 12px; fill: var(--orange); flex: none; }
</style>
</head>
<body>
<main class="canvas">

  <section class="card card--front" aria-label="Card front">
    <div class="figures-backdrop" role="img" aria-label="Faint large silhouette of two standing men"></div>
    <div class="brand">
      <span class="brand__square"></span>
      <span class="brand__name">OAK HARBOR</span>
    </div>
  </section>

  <section class="card card--back" aria-label="Card back">
    <div class="brand">
      <span class="brand__square"></span>
      <span class="brand__name">OAK HARBOR</span>
    </div>

    <h1 class="holder-name">Dorian Kestrup</h1>

    <svg class="divider" width="375" height="18" viewBox="0 0 375 18" aria-hidden="true">
      <line x1="0" y1="9" x2="173" y2="9" stroke="var(--orange)" stroke-width="1.6"/>
      <circle cx="187" cy="9" r="8" fill="var(--orange)"/>
      <line x1="203" y1="9" x2="375" y2="9" stroke="var(--orange)" stroke-width="1.6"/>
    </svg>

    <address class="address">418 W. Linden Ave.,<br>P.O. Box 612, Marlow Bay, FL 32190</address>

    <ul class="contacts">
      <li>
        <svg viewBox="0 0 24 24"><path d="M6.6 10.8a15 15 0 0 0 6.6 6.6l2.2-2.2a1 1 0 0 1 1-.25 11.4 11.4 0 0 0 3.6.57 1 1 0 0 1 1 1V20a1 1 0 0 1-1 1A17 17 0 0 1 3 4a1 1 0 0 1 1-1h3.5a1 1 0 0 1 1 1c0 1.25.2 2.45.57 3.57a1 1 0 0 1-.25 1z"/></svg>
        800-555-0147
      </li>
      <li>
        <svg viewBox="0 0 24 24"><path d="M6 2h12v5H6z M3 8h18a2 2 0 0 1 2 2v7h-4v-3H5v3H1v-7a2 2 0 0 1 2-2z M6 15h12v7H6z"/></svg>
        800-555-0147
      </li>
      <li>
        <svg viewBox="0 0 24 24"><path d="M2 5h20v14H2z" opacity=".9"/><path d="M2 5l10 8 10-8" fill="none" stroke="#fff" stroke-width="1.6"/></svg>
        dorian@oakharbor-legal.com
      </li>
      <li>
        <svg viewBox="0 0 24 24"><circle cx="12" cy="12" r="10"/><path d="M2 12h20M12 2c3 3 3 17 0 20M12 2c-3 3-3 17 0 20" fill="none" stroke="#fff" stroke-width="1.3"/></svg>
        www.oakharbor-legal.com
      </li>
    </ul>
  </section>

</main>
</body>
</html>
```